Home inventory company needs a single full page flyer design for a flyer that will be put into a pre

My company performs home inventory services in case of disaster, or for preparation to move, getting divorced or estate planning. During a free estimate, I will be giving a presentation folder to the customer with this flyer inside. This flyer will be informational in regards to why it is imperative to use my service now vs. later. It should also list the packages I offer, but prices should not go on the flyer as they are subject to change. Flyer should include my logo and colors of the logo. Flyer needs to stand out so unique design ideas are welcome. I see the flyer having a black / dark background and I see the text being a really bright green like in my logo. This is not set in stone though, I anticipate viewing other color schemes.

Target Market(s)

Anyone who lives in a home and owns things

Industry/Entity Type

It Company

Font styles to use
Sans Serif

Requirements
Must have
• My logo, my colors, my packages (without pricing) and some text indicating why my services are needed now vs. later.
Nice to have
• Creativeness with the logo in regards to where it is on the page. I would love to see a gauge or meter next to each home package showing how much coverage each package represents. The meter for the budget package would show that there is adequate coverage. The meter for the last package, grand tucked, would show a meter that is off the charts. In between the meters would show increasing coverage as we get to the end.
Should not have
• There should be nothing in the color white

```html
<!DOCTYPE html>
<html lang="en">
<head>
<meta charset="utf-8">
<title>Tucks Home Inventory Flyer</title>
<link rel="stylesheet" href="https://fonts.googleapis.com/css2?family=Oswald:wght@500;600&family=Open+Sans:wght@400;600;700&display=swap">
<style>
  :root {
    --lime: #8cc63e;
    --lime-dark: #5e9a1f;
    --ink: #0d0f0c;
    --panel: #161a14;
    --text: #d9ddd4;
    --muted: #a9b0a3;
    --sky-top: #6f9fc8;
    --sky-low: #b9cfdf;
    --brick: #8a6a52;
  }
  * { margin: 0; padding: 0; box-sizing: border-box; }
  html, body { width: 857px; height: 1200px; overflow: hidden; background: #2a2d28; }
  .flyer {
    position: relative; width: 857px; height: 1200px; overflow: hidden;
    background: radial-gradient(ellipse at 70% 60%, #1d221a 0%, var(--ink) 70%);
    font-family: "Open Sans", Arial, sans-serif; color: var(--text);
  }
  .hero-photo {
    position: absolute; left: 0; top: 0; width: 857px; height: 470px;
    background: linear-gradient(180deg, var(--sky-top) 0%, var(--sky-low) 38%, #a98c74 55%, var(--brick) 78%, #4f5c3c 100%);
  }
  .headline {
    position: absolute; left: 40px; top: 62px;
    font-family: "Oswald", "Arial Narrow", sans-serif; font-weight: 600;
    font-size: 44px; line-height: 1.08; color: var(--lime);
    text-shadow: 0 2px 3px rgba(0,0,0,.35);
  }
  .swoosh { position: absolute; left: 0; top: 0; }
  .inset {
    position: absolute; border: 3px solid var(--lime);
  }
  .inset-living { left: 40px; top: 418px; width: 205px; height: 150px;
    background: linear-gradient(135deg, #c9a56b, #7e5a36 60%, #3e2d1d); }
  .inset-bedroom { left: 40px; top: 582px; width: 205px; height: 118px;
    background: linear-gradient(135deg, #e4d7c2, #a88c6a 60%, #5a4634); }
  .inset-bedroom2 { left: 255px; top: 500px; width: 160px; height: 200px;
    background: linear-gradient(160deg, #d8cdb8, #9c8466 55%, #4c3a2a); }
  .block { position: absolute; font-size: 9.6px; line-height: 1.38; }
  .block h3 {
    font-family: "Open Sans", Arial, sans-serif; font-weight: 700; font-size: 11px;
    color: var(--lime); text-transform: uppercase; margin-bottom: 4px;
  }
  .block p { margin-bottom: 6px; color: var(--text); }
  .block ul { list-style: none; }
  .block li { position: relative; padding-left: 11px; margin-bottom: 2px; }
  .block li::before {
    content: ""; position: absolute; left: 1px; top: 5px; width: 5px; height: 5px;
    background: var(--lime); border-radius: 50%;
  }
  .col-left { left: 40px; top: 714px; width: 215px; }
  .col-mid-top { left: 430px; top: 500px; width: 158px; }
  .col-mid { left: 270px; top: 760px; width: 318px; }
  .col-right { left: 602px; top: 520px; width: 220px; }
  .note { color: var(--muted); }
  .contact { position: absolute; left: 40px; top: 1032px; font-family: "Open Sans", Arial, sans-serif; }
  .contact-row { display: flex; align-items: center; gap: 10px; font-weight: 700; font-size: 20px; color: var(--lime-dark); margin-bottom: 6px; }
  .contact-row svg { width: 24px; height: 24px; }
  .brand { position: absolute; left: 630px; top: 1062px; display: flex; align-items: center; gap: 10px; }
  .brand-mark { width: 48px; height: 48px; background: var(--lime); }
  .brand-name { font-family: "Open Sans", Arial, sans-serif; font-weight: 700; font-size: 40px; color: var(--lime); letter-spacing: 1px; line-height: 1; }
  .brand-tag { position: absolute; left: 688px; top: 1108px; font-size: 9px; color: var(--muted); }
</style>
</head>
<body>
<div class="flyer">
  <div class="hero-photo" role="img" aria-label="Photo of a brick apartment building with balconies under a blue sky"></div>

  <svg class="swoosh" width="857" height="1200" viewBox="0 0 857 1200" aria-hidden="true">
    <path d="M0 440 C 250 470, 560 420, 857 330 L857 1200 L0 1200 Z" fill="#0d0f0c"/>
    <path d="M0 440 C 250 470, 560 420, 857 330" fill="none" stroke="#8cc63e" stroke-width="7"/>
    <path d="M0 1160 C 260 1130, 520 1170, 857 1120 L857 1200 L0 1200 Z" fill="#8cc63e"/>
    <path d="M0 1180 C 300 1150, 560 1190, 857 1150 L857 1200 L0 1200 Z" fill="#5e9a1f"/>
  </svg>

  <h1 class="headline">Get Your House Tucked<br>Before It's Too Late...</h1>

  <div class="inset inset-living" role="img" aria-label="Photo of a furnished living room"></div>
  <div class="inset inset-bedroom" role="img" aria-label="Photo of a tidy bedroom"></div>
  <div class="inset inset-bedroom2" role="img" aria-label="Photo of a bedroom interior"></div>

  <section class="block col-mid-top">
    <h3>Grand Tucked Package</h3>
    <ul>
      <li>Detailed photos and documentation of every room in your home</li>
      <li>Serial numbers of large appliances and electronics recorded</li>
      <li>Back-up copy of inventory on disc</li>
      <li>Full inventory binder with report and photos</li>
      <li>Up to 3,000 items</li>
      <li>Free update within the first 12 months</li>
    </ul>
  </section>

  <section class="block col-right">
    <p class="note">*** Packages above reflect pricing for homes up to 2,500 square feet. Homes above 2,500 square feet will be charged for each extra room.</p>
    <p class="note">*** If your home has an above average amount of contents, the amount of photos needed to document your items may exceed a standard package. If additional photos are required, there will be a charge for each extra photo block, which is discussed in advance.</p>
    <h3 style="margin-top:10px">Additional Services</h3>
    <ul>
      <li>Clothing inventory: all packages include general photos of closets and shoe boxes.</li>
      <li>Jewelry, artwork, collectibles: individual photos and written descriptions of every piece.</li>
      <li>Receipts and warranty copies scanned and added to your report.</li>
      <li>Estate planning and relocation assistance.</li>
      <li>Annual update: photos of new items only.</li>
      <li>Business inventory services by quote.</li>
    </ul>
  </section>

  <section class="block col-left">
    <h3>Apartment Package <span style="text-transform:none;font-weight:600">(for apartments only)</span></h3>
    <ul>
      <li>Detailed photos and documentation of larger valued items such as electronics and furniture</li>
      <li>Back-up copy of inventory on disc</li>
      <li>Inventory report with photos</li>
      <li>Up to 500 items</li>
    </ul>
    <h3 style="margin-top:10px">Small Package</h3>
    <ul>
      <li>Detailed photos and documentation of larger valued items such as electronics and furniture, plus serial numbers where available</li>
      <li>Back-up copy of inventory on disc</li>
      <li>Inventory report with photos</li>
      <li>Up to 1,000 items</li>
    </ul>
  </section>

  <section class="block col-mid">
    <h3>Fully Tucked Package</h3>
    <ul>
      <li>Detailed photos and documentation of each household item, plus general photos of every room, closet and drawer</li>
      <li>Serial numbers of large appliances and electronics recorded</li>
      <li>Back-up copy of inventory on disc</li>
      <li>Full inventory binder with report and photos</li>
      <li>Up to 2,000 items</li>
      <li>Free update within the first 12 months</li>
      <li>Includes all additional services listed below except for the additional photo blocks</li>
    </ul>
  </section>

  <div class="contact">
    <div class="contact-row">
      <svg viewBox="0 0 24 24" aria-hidden="true"><path fill="#5e9a1f" d="M6.6 10.8a15 15 0 0 0 6.6 6.6l2.2-2.2c.3-.3.7-.4 1-.2 1.1.4 2.3.6 3.6.6.6 0 1 .4 1 1V20c0 .6-.4 1-1 1A17 17 0 0 1 3 4c0-.6.4-1 1-1h3.5c.6 0 1 .4 1 1 0 1.3.2 2.5.6 3.6.1.3 0 .7-.2 1z"/></svg>
      <span>555-014-2273</span>
    </div>
    <div class="contact-row">
      <svg viewBox="0 0 24 24" aria-hidden="true"><rect x="2" y="5" width="20" height="14" rx="2" fill="#5e9a1f"/><path d="M3 6l9 7 9-7" fill="none" stroke="#0d0f0c" stroke-width="1.6"/></svg>
      <span>dan@tuckshouse.com</span>
    </div>
    <div class="contact-row">
      <svg viewBox="0 0 24 24" aria-hidden="true"><circle cx="12" cy="12" r="10" fill="#5e9a1f"/><path d="M2 12h20M12 2c3 3 3 17 0 20M12 2c-3 3-3 17 0 20" fill="none" stroke="#0d0f0c" stroke-width="1.4"/></svg>
      <span>www.tuckshouse.com</span>
    </div>
  </div>

  <div class="brand">
    <div class="brand-mark" aria-hidden="true"></div>
    <div class="brand-name">TUCKS</div>
  </div>
  <div class="brand-tag">Tucks Home Inventory Services</div>
</div>
</body>
</html>
```